Brenmoor Group needs a business card

I would like the card to be simple but modern and elegant.
I like black and white.
or black and gold.
we are a private finance lender and also are involved in property and property developments.

please look at the business card photos i provided i would like B.G only one one side and all the other details on the other side use fonts that tie in with my theme.

Industry/Entity Type

Finance

Contact Information for Business Card

Brenmoor Group (B.G) Callum Brenmoor M: 0418396152 E: callumbren@quivomail.com

Font styles to use
Other font styles liked:
• Use fonts that would reflect our business

Colors
000000
ffffff

Requirements
Must have
• one side of details
• other side has either B.G or Brenmoor Group like in the photos provided

```html
<!DOCTYPE html>
<html lang="en">
<head>
<meta charset="utf-8">
<title>Brenmoor Group – Business Card</title>
<link rel="stylesheet" href="https://fonts.googleapis.com/css2?family=Open+Sans:wght@400;700&display=swap">
<style>
  :root {
    --backdrop: #6e4c35;
    --card-white: #ffffff;
    --card-black: #000000;
    --ink: #000000;
    --ink-soft: #555555;
    --reverse: #ffffff;
  }
  * { box-sizing: border-box; margin: 0; padding: 0; }
  html, body {
    width: 1200px;
    height: 987px;
    overflow: hidden;
  }
  body {
    position: relative;
    background: var(--backdrop);
    font-family: "Open Sans", Arial, sans-serif;
  }
  .card {
    position: absolute;
    left: 293px;
    width: 615px;
    height: 351px;
    box-shadow: 0 3px 8px rgba(0,0,0,0.35);
  }
  .card--front { top: 130px; background: var(--card-white); }
  .card--back  { top: 506px; background: var(--card-black); }

  .name-band {
    position: absolute;
    left: 0;
    top: 183px;
    width: 302px;
    height: 58px;
    background: var(--card-black);
    clip-path: polygon(0 0, 279px 0, 302px 100%, 0 100%);
    display: flex;
    align-items: center;
    padding-left: 31px;
  }
  .name-band__text {
    color: var(--reverse);
    font-weight: 700;
    font-size: 22px;
    letter-spacing: 0.3px;
    text-transform: uppercase;
    white-space: nowrap;
  }

  .contact-list {
    position: absolute;
    left: 32px;
    top: 256px;
    list-style: none;
  }
  .contact-list__item {
    display: flex;
    align-items: center;
    height: 23px;
    color: var(--ink-soft);
    font-size: 16px;
  }
  .contact-list__icon {
    width: 15px;
    height: 15px;
    margin-right: 9px;
    flex: none;
  }

  .company-name {
    position: absolute;
    inset: 0;
    display: flex;
    align-items: center;
    justify-content: center;
    color: var(--reverse);
    font-weight: 700;
    font-size: 46px;
    letter-spacing: 0.5px;
    text-transform: uppercase;
    line-height: 1;
  }
</style>
</head>
<body>
  <section class="card card--front" aria-label="Business card front">
    <div class="name-band"><span class="name-band__text">Callum Brenmoor</span></div>
    <ul class="contact-list">
      <li class="contact-list__item">
        <svg class="contact-list__icon" viewBox="0 0 16 16" aria-hidden="true">
          <rect x="4" y="1" width="8" height="14" rx="1.5" fill="var(--ink)"/>
          <rect x="5.5" y="3" width="5" height="9" fill="var(--card-white)"/>
        </svg>
        0418396152
      </li>
      <li class="contact-list__item">
        <svg class="contact-list__icon" viewBox="0 0 16 16" aria-hidden="true">
          <rect x="1" y="4" width="14" height="9" fill="var(--ink)"/>
          <path d="M1.5 4.5 L8 9.5 L14.5 4.5" stroke="var(--card-white)" stroke-width="1.2" fill="none"/>
        </svg>
        callumbren@quivomail.com
      </li>
      <li class="contact-list__item">
        <svg class="contact-list__icon" viewBox="0 0 16 16" aria-hidden="true">
          <circle cx="8" cy="8" r="6.5" fill="var(--ink)"/>
          <ellipse cx="8" cy="8" rx="2.6" ry="6.5" stroke="var(--card-white)" stroke-width="0.9" fill="none"/>
          <path d="M1.5 8 H14.5" stroke="var(--card-white)" stroke-width="0.9"/>
        </svg>
        www.brenmoorgroup.com
      </li>
    </ul>
  </section>

  <section class="card card--back" aria-label="Business card back">
    <div class="company-name">Brenmoor Group</div>
  </section>
</body>
</html>
```